Restaurant needs a vertical banner for fried catfish

Our restaurant is looking for an eye-catching 78.75in. x 36in. vertical physical banner ad for our fried catfish. Photos for the fried catfish will be provided as a reference but we will also accept anything similar to the photo. We will be using the following as our receptacle: https://www.plankoria.example/banner-stand/retractable-banner-stands/
The design must incorporate the following flavor texts:
Fried Catfish
Always Fresh!
Made from Scratch
Hand-cut Fillets
The Best Catfish in Texas
Served with fries, hush puppies, and a 32oz fountain drink
Also available by the pound!
The final design should be creative, professional, and eye-catching for customers.
Updates
Colors
Designer to choose colors to be used in the design.
Requirements
Must have
- We are open to any and all design elements, albeit the 'flavor texts' should not overpower, but complement the fried catfish photo. 'Fried Catfish' can be used in lieu of a main title/logo.
Nice to have
- Transparent or textured backgrounds that can encompass any or all part of the banner such as a cutting board, shadows, abstract, etc to show depth are a plus.
- Use of vectors or objects such as ribbons or shapes to encapsulate the 'flavor texts' are also encouraged.

```html
<!DOCTYPE html>
<html lang="en">
<head>
<meta charset="utf-8">
<title>Fried Catfish Banner</title>
<link rel="stylesheet" href="https://fonts.googleapis.com/css2?family=Saira+Extra+Condensed:wght@700&family=Fira+Sans+Extra+Condensed:ital,wght@1,400&family=Arimo:wght@700&display=swap">
<style>
  :root {
    --stage: #767676;
    --blue-light: #1f5b87;
    --blue-mid: #0a4770;
    --blue-deep: #07334f;
    --gold: #e6b24e;
    --white: #ffffff;
    --ink: #1a1a1a;
  }
  * { margin: 0; padding: 0; box-sizing: border-box; }
  html, body { width: 1200px; height: 1200px; overflow: hidden; background: var(--stage); }
  .canvas { position: relative; width: 1200px; height: 1200px; }
  .banner {
    position: absolute; left: 338px; top: 29px;
    width: 523px; height: 1142px; overflow: hidden;
    background: var(--blue-light);
  }
  .banner-art { position: absolute; inset: 0; }
  .title-text {
    font-family: "Saira Extra Condensed", "Arial Narrow", sans-serif;
    font-weight: 700;
    fill: var(--gold);
    stroke: var(--white);
    stroke-width: 1.6;
    paint-order: stroke;
  }
  .logo-text {
    font-family: "Saira Extra Condensed", "Arial Narrow", sans-serif;
    font-weight: 700; fill: var(--ink);
  }
  .features {
    position: absolute; left: 35px; top: 814px;
    list-style: none;
    font-family: "Fira Sans Extra Condensed", "Arial Narrow", sans-serif;
    font-style: italic; font-weight: 400;
    font-size: 24px; line-height: 32.5px;
    color: var(--white);
  }
  .features li { position: relative; padding-left: 21px; }
  .features li::before {
    content: ""; position: absolute; left: 0; top: 11px;
    width: 11px; height: 11px; background: var(--gold);
  }
  .footer-band {
    position: absolute; left: 0; bottom: 0; width: 100%; height: 71px;
    background: var(--blue-light);
    display: flex; align-items: center; justify-content: center;
  }
  .web-address {
    font-family: "Arimo", Arial, sans-serif; font-weight: 700;
    font-size: 27px; letter-spacing: 2.5px; color: var(--gold);
  }
</style>
</head>
<body>
<div class="canvas">
  <section class="banner">
    <svg class="banner-art" width="523" height="1142" viewBox="0 0 523 1142">
      <defs>
        <radialGradient id="plate-tone" cx="55%" cy="45%" r="60%">
          <stop offset="0" stop-color="#b8772e"/>
          <stop offset="0.55" stop-color="#d9a24e"/>
          <stop offset="1" stop-color="#f2ede4"/>
        </radialGradient>
        <linearGradient id="side-tone" x1="0" y1="0" x2="0" y2="1">
          <stop offset="0" stop-color="#d4a457"/>
          <stop offset="1" stop-color="#a8702e"/>
        </linearGradient>
        <linearGradient id="garnish-tone" x1="0" y1="0" x2="0" y2="1">
          <stop offset="0" stop-color="#d9553b"/>
          <stop offset="0.35" stop-color="#e7e2d8"/>
          <stop offset="1" stop-color="#b9823c"/>
        </linearGradient>
      </defs>

      <path class="wave-mid" fill="var(--blue-mid)"
        d="M0 230 C30 300 70 330 110 318 C170 300 230 330 270 380 C320 440 380 430 440 400 C480 385 505 390 523 410 L523 1142 L0 1142 Z"/>
      <path class="wave-deep" fill="var(--blue-deep)"
        d="M0 870 C40 850 80 800 160 790 C230 780 250 860 290 870 C350 885 420 850 523 840 L523 1142 L0 1142 Z"/>

      <g transform="translate(33 216) skewX(-7)">
        <text class="title-text" x="0" y="0" font-size="230" textLength="282" lengthAdjust="spacingAndGlyphs">FRIED</text>
      </g>
      <g transform="translate(33 409) skewX(-7)">
        <text class="title-text" x="0" y="0" font-size="230" textLength="428" lengthAdjust="spacingAndGlyphs">CATFISH</text>
      </g>

      <g class="logo-mark">
        <ellipse cx="429" cy="136" rx="73" ry="65" fill="var(--white)"/>
        <text class="logo-text" x="429" y="154" font-size="50" text-anchor="middle" textLength="82" lengthAdjust="spacingAndGlyphs">LOGO</text>
      </g>

      <g role="img" aria-label="Photo of fried catfish fillets on a white plate with fries, hush puppies and tartar sauce">
        <path fill="url(#plate-tone)"
          d="M10 600 C20 520 90 470 180 450 C260 430 380 420 523 445 L523 700 C470 740 380 760 280 757 C170 755 60 730 20 680 C8 660 4 630 10 600 Z"/>
      </g>

      <g role="img" aria-label="Close-up photo of fried catfish with fries">
        <circle cx="298" cy="804" r="73" fill="url(#side-tone)" stroke="var(--white)" stroke-width="3"/>
      </g>
      <g role="img" aria-label="Photo of seasoned catfish fillets with tomatoes and lemons">
        <circle cx="438" cy="763" r="86" fill="url(#garnish-tone)" stroke="var(--white)" stroke-width="3"/>
      </g>

      <g class="price">
        <g transform="translate(341 952) skewX(-6)">
          <text class="title-text" x="0" y="0" font-size="95" textLength="22" lengthAdjust="spacingAndGlyphs">$</text>
        </g>
        <g transform="translate(360 1043) skewX(-6)">
          <text class="title-text" x="0" y="0" font-size="220" textLength="112" lengthAdjust="spacingAndGlyphs">99</text>
        </g>
      </g>
    </svg>

    <ul class="features">
      <li>Always Fresh!</li>
      <li>Made from Scratch</li>
      <li>Hand-cut Fillets</li>
      <li>The Best Catfish in Texas</li>
      <li>Served with fries, hush puppies,<br>and a 32oz fountain drink</li>
      <li>Also available by the pound!</li>
    </ul>

    <footer class="footer-band">
      <span class="web-address">www.fryhouse.example</span>
    </footer>
  </section>
</div>
</body>
</html>
```